Diabetes control iOS/Android app design

I need a modern app design with light colors that are easy on the eyes, This app is for diabetes control. Focusing on Sweet/carb control and its daily intake .. I have uploaded some wireframe pages to design . Light colors are preferred for design. I donot need too much Hussle and data on main page.
Name/title: Glucaro- Diabetes reversal

Target Market(s)

Diabetes patients

Industry/Entity Type

health

Colors
0094D4
00A9DD
6FCCEA
C7EBF8
E9F6FB
00AB8E
00BBA5
67D7C9
C6EFE9
E9F9F6
59FF00
82FF00
B8FF75
E3FFCB
F4FFEA
FFC000
F8CF3A
FAE287
FDF2CF
FEFAEE

Requirements
Should not have
• complicated design. It should be simple , modern and easy o eye.

```html
<!DOCTYPE html>
<html lang="en">
<head>
<meta charset="utf-8">
<title>Diabetes control app screens</title>
<link rel="stylesheet" href="https://fonts.googleapis.com/css2?family=Inter:wght@400;500;600;700;800;900&display=swap">
<style>
  :root{
    --board:#363f48;
    --screen:#eeeeee;
    --white:#ffffff;
    --ink:#111111;
    --muted:#7a7a7a;
    --green:#3daf84;
    --grey-line:#6f6f6f;
    --blue:#0499d8;
    --ring:#e4e4e4;
    --red:#ff0000;
    --drop:#f26672;
    --seg1:#ff9a9a;
    --seg2:#ff5f4f;
    --seg3:#ff0000;
    --seg4:#b00f0f;
    --seg5:#5e1710;
    --grid:#dddddd;
  }
  *{box-sizing:border-box;margin:0;padding:0}
  html,body{width:1200px;height:968px;overflow:hidden;background:#ffffff}
  body{font-family:"Inter",sans-serif;color:var(--ink)}
  .board{position:absolute;left:0;top:0;width:1200px;height:968px;background:var(--board);border-radius:28px;overflow:hidden}
  .phone{position:absolute;top:192px;width:319px;height:690px;border-radius:33px;background:var(--screen);overflow:hidden}
  .phone--today{left:90px}
  .phone--monitor{left:440.5px}
  .phone--feed{left:790.7px}
  .status{position:absolute;left:0;top:0;width:100%;height:36px}
  .status__time{position:absolute;left:19px;top:10px;font-size:12.5px;font-weight:500}
  .status__icons{position:absolute;right:20px;top:12px}
  .screen-title{position:absolute;left:0;width:100%;top:64px;text-align:center;font-size:20px;font-weight:700}
  .pager{position:absolute;top:70px}
  .abs{position:absolute}
  .gauge-label{position:absolute;left:0;width:319px;text-align:center}
  .gauge-label--title{top:205px;font-size:13.5px;font-weight:600}
  .gauge-label--value{top:225px;font-size:65px;font-weight:900;letter-spacing:-1px;line-height:1}
  .gauge-label--unit{top:294px;font-size:13px;font-weight:500}
  .today-lower{position:absolute;left:0;top:452px;width:100%;height:238px;background:var(--white)}
  .section-title{position:absolute;left:0;width:100%;text-align:center;font-size:15px;font-weight:600}
  .scale{position:absolute;left:19.5px;top:102px;width:280px;height:15px;display:flex}
  .scale span{flex:1}
  .scale-labels{position:absolute;left:19.5px;top:125px;width:280px;font-size:10px;font-weight:600;display:flex;justify-content:space-between}
  .tabbar{position:absolute;left:0;top:613px;width:100%;height:77px;background:var(--white);border-top:1px solid #e8e8e8}
  .tabbar svg{position:absolute;left:0;top:0}
  .home-indicator{position:absolute;left:77.5px;top:67px;width:164px;height:5px;border-radius:3px;background:#111}
  .card{position:absolute;left:19.5px;width:280px;background:var(--white);border-radius:3px}
  .card--sugar{top:121px;height:261px}
  .card--walk{top:398px;height:167px}
  .card__title{position:absolute;left:13px;top:13px;font-size:13px;font-weight:600}
  .segmented{position:absolute;left:13px;top:38px;width:254px;height:20px;border-radius:10px;background:#eeeeee;display:flex;font-size:6.5px;font-weight:500;color:#777777}
  .segmented span{flex:1;display:flex;align-items:center;justify-content:center;position:relative}
  .segmented .sep{border-left:0.8px solid #c9c9c9}
  .segmented .is-active{background:var(--green);color:#fff;border-radius:10px;font-weight:600}
  .legend{position:absolute;top:70px;font-size:6.5px;font-weight:500;padding-bottom:3px}
  .legend--fasting{left:161px;color:var(--green);border-bottom:1.5px solid var(--green)}
  .legend--random{left:218px;color:#666666;border-bottom:1.5px solid #777777}
  .caption{position:absolute;left:0;width:100%;top:580px;text-align:center;font-size:12px;font-weight:500}
  .field-label{position:absolute;left:19.5px;font-size:13px;font-weight:600}
  .field-hint{position:absolute;left:19.5px;font-size:10px;font-weight:500;color:var(--muted)}
  .field-input{position:absolute;left:191px;width:108px;height:39px;background:var(--white);border-radius:3px}
  .submit{position:absolute;left:0;top:613px;width:100%;height:77px;background:var(--blue);border:0;border-radius:24px 24px 33px 33px;color:#fff;font-family:inherit;font-size:20px;font-weight:600;display:flex;align-items:center;justify-content:center}
</style>
</head>
<body>
<main class="board">

  <!-- Today screen -->
  <section class="phone phone--today">
    <div class="status">
      <span class="status__time">9:41</span>
      <svg class="status__icons" width="55" height="10" viewBox="0 0 55 10">
        <rect x="0" y="6" width="2.5" height="3" fill="#111"/><rect x="4" y="4.5" width="2.5" height="4.5" fill="#111"/><rect x="8" y="2.5" width="2.5" height="6.5" fill="#111"/><rect x="12" y="0.5" width="2.5" height="8.5" fill="#111"/>
        <path d="M19 3.5a8 8 0 0 1 11 0M21 5.5a5 5 0 0 1 7 0M23.3 7.5a1.8 1.8 0 0 1 2.4 0" stroke="#111" stroke-width="1.5" fill="none"/>
        <rect x="36" y="1" width="16" height="8" rx="2" fill="none" stroke="#999" stroke-width="0.8"/><rect x="37.5" y="2.5" width="13" height="5" rx="1" fill="#111"/><rect x="52.5" y="3.5" width="1.5" height="3" fill="#999"/>
      </svg>
    </div>
    <svg class="pager" style="left:24px" width="10" height="14" viewBox="0 0 10 14"><path d="M8 1 2 7l6 6" stroke="#111" stroke-width="1.6" fill="none"/></svg>
    <h1 class="screen-title">Today</h1>
    <svg class="pager" style="left:285px" width="10" height="14" viewBox="0 0 10 14"><path d="M2 1l6 6-6 6" stroke="#111" stroke-width="1.6" fill="none"/></svg>

    <svg class="abs" style="left:0;top:0" width="319" height="452" viewBox="0 0 319 452" aria-hidden="true">
      <circle cx="159" cy="260" r="109" fill="var(--white)" stroke="var(--ring)" stroke-width="10"/>
      <circle cx="159" cy="260" r="109" fill="none" stroke="var(--red)" stroke-width="10" stroke-dasharray="236 685" transform="rotate(-90 159 260)"/>
      <circle cx="159" cy="363" r="31" fill="var(--white)" stroke="var(--drop)" stroke-width="3.5"/>
      <path d="M159 347c-6 8-10 13-10 18a10 10 0 0 0 20 0c0-5-4-10-10-18z" fill="var(--drop)"/>
      <path d="M159 359l5 2.5v5.5l-5 2.5-5-2.5v-5.5z" fill="#dfe9ff"/>
    </svg>
    <div class="gauge-label gauge-label--title">Blood Count</div>
    <div class="gauge-label gauge-label--value">128</div>
    <div class="gauge-label gauge-label--unit">mg/dL</div>

    <div class="today-lower">
      <h2 class="section-title" style="top:26px">Consumption Today</h2>
      <svg class="abs" style="left:145px;top:66px" width="24" height="28" viewBox="0 0 24 28" aria-hidden="true">
        <path d="M12 26C5 18 2 14 2 10a10 10 0 0 1 20 0c0 4-3 8-10 16z" fill="none" stroke="var(--red)" stroke-width="2"/>
        <circle cx="12" cy="10" r="3.5" fill="none" stroke="var(--red)" stroke-width="2"/>
      </svg>
      <div class="scale">
        <span style="background:var(--seg1)"></span><span style="background:var(--seg2)"></span><span style="background:var(--seg3)"></span><span style="background:var(--seg4)"></span><span style="background:var(--seg5)"></span>
      </div>
      <div class="scale-labels"><span>Danger</span><span>Fatal</span><span>Catastrophic</span></div>
    </div>

    <nav class="tabbar">
      <svg width="319" height="77" viewBox="0 0 319 77" aria-hidden="true">
        <g fill="none" stroke-width="1.6" stroke-linejoin="round">
          <path d="M33 28l8-7 8 7v10H33z M38.5 38v-6h5v6" stroke="var(--green)"/>
          <path d="M85 29h4l3-6 4 12 3-6h5" stroke="#111"/>
          <path d="M215 22c3-1.5 6-1.5 8 0.5 2-2 5-2 8-0.5v14c-3-1.5-6-1.5-8 0.5-2-2-5-2-8-0.5z M223 22.5v14" stroke="#111"/>
          <circle cx="277" cy="24" r="4" stroke="#111"/><path d="M269 37c1-5 4-7 8-7s7 2 8 7" stroke="#111"/>
        </g>
        <circle cx="159" cy="29" r="20" fill="var(--blue)"/>
        <path d="M159 21v16M151 29h16" stroke="#fff" stroke-width="2.6"/>
      </svg>
      <span class="home-indicator"></span>
    </nav>
  </section>

  <!-- Rehab Monitor screen -->
  <section class="phone phone--monitor">
    <div class="status">
      <span class="status__time">9:41</span>
      <svg class="status__icons" width="55" height="10" viewBox="0 0 55 10">
        <rect x="0" y="6" width="2.5" height="3" fill="#111"/><rect x="4" y="4.5" width="2.5" height="4.5" fill="#111"/><rect x="8" y="2.5" width="2.5" height="6.5" fill="#111"/><rect x="12" y="0.5" width="2.5" height="8.5" fill="#111"/>
        <path d="M19 3.5a8 8 0 0 1 11 0M21 5.5a5 5 0 0 1 7 0M23.3 7.5a1.8 1.8 0 0 1 2.4 0" stroke="#111" stroke-width="1.5" fill="none"/>
        <rect x="36" y="1" width="16" height="8" rx="2" fill="none" stroke="#999" stroke-width="0.8"/><rect x="37.5" y="2.5" width="13" height="5" rx="1" fill="#111"/><rect x="52.5" y="3.5" width="1.5" height="3" fill="#999"/>
      </svg>
    </div>
    <h1 class="screen-title">Rehab Monitor</h1>

    <article class="card card--sugar">
      <h2 class="card__title">Daily Sugar</h2>
      <div class="segmented">
        <span class="is-active">Day</span><span>Week</span><span class="sep">Month</span><span class="sep">Year</span>
      </div>
      <span class="legend legend--fasting">Fasting Sugar</span>
      <span class="legend legend--random">Random Sugar</span>
      <svg class="abs" style="left:-19.5px;top:-121px" width="319" height="390" viewBox="0 0 319 390" aria-label="Fasting and random sugar line chart" role="img">
        <g font-family="Inter, sans-serif" font-size="6.5" fill="#222222" text-anchor="end">
          <text x="45" y="216">180</text><text x="45" y="233">170</text><text x="45" y="249">160</text><text x="45" y="265">150</text><text x="45" y="282">140</text><text x="45" y="298">130</text><text x="45" y="315">120</text><text x="45" y="331">110</text><text x="45" y="347">100</text><text x="45" y="364">90</text>
        </g>
        <path d="M53.5 194v173" stroke="#cfcfcf" stroke-width="0.8" stroke-dasharray="2 2"/>
        <path d="M53.5 367H282" stroke="#cfcfcf" stroke-width="0.8" stroke-dasharray="2 2"/>
        <path d="M53.5 338C75 328 98 300 117 282S140 271 150 271S175 274 184 272S198 266 206 260S228 237 245 236S270 235 280 235" fill="none" stroke="var(--grey-line)" stroke-width="1.4"/>
        <path d="M53.5 363C62 362 68 363 75 356S88 338 95 330S112 306 128 304S170 301 184 301S198 296 206 290S225 271 240 270S268 268 280 268" fill="none" stroke="var(--green)" stroke-width="1.4"/>
      </svg>
    </article>

    <article class="card card--walk">
      <svg class="abs" style="left:-19.5px;top:-398px" width="319" height="570" viewBox="0 0 319 570" aria-label="Daily walk and exercise bar chart" role="img">
        <g stroke="var(--grid)" stroke-width="0.8" stroke-dasharray="3 2">
          <path d="M19.5 423H300M19.5 447H300M19.5 472H300M19.5 497H300M19.5 521H300M19.5 546H300"/>
        </g>
        <g fill="var(--green)">
          <rect x="29" y="523.6" width="40.7" height="41.4" rx="1.5"/>
          <rect x="73" y="469" width="40.7" height="96" rx="1.5"/>
          <rect x="117" y="495.7" width="40.7" height="69.3" rx="1.5"/>
          <rect x="161.7" y="523.6" width="40.7" height="41.4" rx="1.5"/>
          <rect x="205.8" y="542" width="40.7" height="23" rx="1.5"/>
          <rect x="249.8" y="488" width="40.7" height="77" rx="1.5"/>
        </g>
      </svg>
    </article>
    <p class="caption">Daily walk/exercise</p>

    <nav class="tabbar">
      <svg width="319" height="77" viewBox="0 0 319 77" aria-hidden="true">
        <g fill="none" stroke-width="1.6" stroke-linejoin="round">
          <path d="M33 28l8-7 8 7v10H33z M38.5 38v-6h5v6" stroke="#111"/>
          <path d="M85 29h4l3-6 4 12 3-6h5" stroke="var(--green)"/>
          <path d="M215 22c3-1.5 6-1.5 8 0.5 2-2 5-2 8-0.5v14c-3-1.5-6-1.5-8 0.5-2-2-5-2-8-0.5z M223 22.5v14" stroke="#111"/>
          <circle cx="277" cy="24" r="4" stroke="#111"/><path d="M269 37c1-5 4-7 8-7s7 2 8 7" stroke="#111"/>
        </g>
        <circle cx="159" cy="29" r="20" fill="var(--blue)"/>
        <path d="M159 21v16M151 29h16" stroke="#fff" stroke-width="2.6"/>
      </svg>
      <span class="home-indicator"></span>
    </nav>
  </section>

  <!-- Daily Feed screen -->
  <section class="phone phone--feed">
    <div class="status">
      <span class="status__time">9:41</span>
      <svg class="status__icons" width="55" height="10" viewBox="0 0 55 10">
        <rect x="0" y="6" width="2.5" height="3" fill="#111"/><rect x="4" y="4.5" width="2.5" height="4.5" fill="#111"/><rect x="8" y="2.5" width="2.5" height="6.5" fill="#111"/><rect x="12" y="0.5" width="2.5" height="8.5" fill="#111"/>
        <path d="M19 3.5a8 8 0 0 1 11 0M21 5.5a5 5 0 0 1 7 0M23.3 7.5a1.8 1.8 0 0 1 2.4 0" stroke="#111" stroke-width="1.5" fill="none"/>
        <rect x="36" y="1" width="16" height="8" rx="2" fill="none" stroke="#999" stroke-width="0.8"/><rect x="37.5" y="2.5" width="13" height="5" rx="1" fill="#111"/><rect x="52.5" y="3.5" width="1.5" height="3" fill="#999"/>
      </svg>
    </div>
    <h1 class="screen-title">Daily Feed</h1>

    <span class="field-label" style="top:124px">Fasting Sugar</span>
    <span class="field-hint" style="top:144px">in mg/dL</span>
    <span class="field-input" style="top:121px"></span>

    <span class="field-label" style="top:176px">Random Sugar</span>
    <span class="field-hint" style="top:196px">in mg/dL</span>
    <span class="field-input" style="top:173px"></span>

    <span class="field-label" style="top:229px">Daily walk/excercise</span>
    <span class="field-hint" style="top:249px">in Minutes</span>
    <span class="field-input" style="top:225px"></span>

    <button class="submit" type="button">Submit</button>
  </section>

</main>
</body>
</html>
```